PDF flyer to go out to Medical Providers: 2 sided A4

We need to design a 2 sided A4 pamphlet which we can email out to prospective clients.

We are a recruitment company and wish to provide staff to healthcare providers

We are a medical recruitment agency. We need to be able to write approximately 600 words, split up into 4 sub headings. Text has been provided on the uploaded word document. THIS TEXT IS DRAFT ONLY AND WILL CHANGE.

We need to look professional & efficient

Target Market(s)

Hospitals, srugeries

Industry/Entity Type

Medical

Requirements
Must have
• Room for 600 words, which will b echanged once the layout is confirmed
Nice to have
• Have it in Word form so we can use it for subsequent mail outs.

```html
<!DOCTYPE html>
<html lang="en">
<head>
<meta charset="utf-8">
<title>Meridian Care Staffing – Two-Page Flyer</title>
<link href="https://fonts.googleapis.com/css2?family=Arimo:wght@400;700&family=Oswald:wght@400;500&display=swap" rel="stylesheet">
<style>
:root{
  --backdrop:#3a3d3b;
  --paper:#ffffff;
  --teal:#2e7275;
  --green:#1fa84a;
  --ink:#222222;
  --white:#ffffff;
  --photo-light:#e4ecee;
  --photo-mid:#b9cfd3;
}
*{box-sizing:border-box;margin:0;padding:0}
html,body{width:1200px;height:857px;overflow:hidden;background:var(--backdrop)}
body{position:relative;font-family:'Arimo',Arial,sans-serif;color:var(--ink)}
.page{position:absolute;top:80px;width:490px;height:694px;background:var(--paper);overflow:hidden}
.page--front{left:77px}
.page--back{left:626px}
.abs{position:absolute}
.body-text{font-size:9.4px;line-height:12px;text-align:justify}
.photo{position:absolute;background:linear-gradient(135deg,var(--photo-light),var(--photo-mid))}
.foot-rule{position:absolute;left:0;right:0;top:684px;height:3px;background:var(--green)}

/* front */
.brand{left:36px;top:34px;display:flex;align-items:center;gap:9px;color:var(--teal);font-size:25px;font-weight:400;letter-spacing:.3px}
.brand__dot{width:28px;height:28px;border-radius:50%;background:var(--teal)}
.hero-photo{left:0;top:85px;width:490px;height:261px}
.title-band{left:0;top:346px;width:490px;height:62px;background:var(--teal)}
.title-band h1{position:absolute;left:16px;top:9px;font-family:'Oswald',sans-serif;font-weight:500;color:var(--white);font-size:18px;line-height:22px;letter-spacing:.2px}
.spec-box{left:274px;top:322px;width:199px;height:272px;background:var(--green);color:var(--white)}
.spec-photo{left:3px;top:5px;width:193px;height:81px}
.spec-intro{position:absolute;left:7px;top:94px;width:177px;font-size:9.6px;line-height:12px;text-align:justify}
.spec-intro b{font-family:'Oswald',sans-serif;font-weight:400;font-size:10.5px}
.spec-list{position:absolute;left:46px;top:153px;width:142px;list-style:none;font-size:8.4px;line-height:10.8px}
.spec-list li{position:relative}
.spec-list li::before{content:"✓";position:absolute;left:-13px}
.about{left:16px;top:424px;width:236px}
.about p+p{margin-top:12px}
.service-clock{left:19px;top:603px}
.service-tag{left:37px;top:624px;background:var(--teal);color:var(--white);font-family:'Oswald',sans-serif;font-size:10.5px;line-height:14px;padding:0 3px;white-space:nowrap}
.service-text{left:143px;top:625px;width:329px}

/* back */
.head-band{left:0;top:13px;width:490px;height:70px;background:var(--teal);color:var(--white)}
.head-band h2{position:absolute;left:26px;top:9px;font-family:'Oswald',sans-serif;font-weight:500;font-size:19px;letter-spacing:.3px}
.head-band h3{position:absolute;left:27px;top:43px;font-family:'Arimo',sans-serif;font-weight:700;font-size:14px}
.lead{left:22px;top:98px;width:448px}
.lead .kick{color:var(--teal);font-weight:700;font-size:13px}
.para2{left:22px;top:134px;width:448px}
.drive-head{left:21px;top:190px;width:230px;color:var(--teal);font-weight:700;font-size:13px;line-height:16px}
.drive-photo{left:250px;top:187px;width:240px;height:154px}
.drive-list{left:22px;top:226px;width:214px}
.drive-list p+p{margin-top:9px}
.market{left:22px;top:338px;width:448px}
.screen-band{left:0;top:432px;width:226px;height:25px;background:var(--teal);color:var(--white);font-weight:700;font-size:13px;padding:5px 0 0 22px}
.screen-note{left:22px;top:466px;font-size:9.4px;font-weight:700}
.screen-band-green{left:0;top:480px;width:490px;height:184px;background:var(--green);color:var(--white)}
.screen-col{position:absolute;top:48px;font-size:9.6px;line-height:11.9px}
.screen-icon{position:absolute;top:6px}
</style>
</head>
<body>

<section class="page page--front">
  <div class="abs brand"><span class="brand__dot"></span><span>Meridian Care Staffing</span></div>
  <div class="photo hero-photo" role="img" aria-label="Photo of a smiling team of doctors and nurses in white coats and scrubs"></div>
  <div class="abs title-band"><h1>A SPECIALIST TEAM<br>DEDICATED TO SPECIAL CARE</h1></div>
  <div class="abs spec-box">
    <div class="photo spec-photo" role="img" aria-label="Photo of a nurse with colleagues working in a bright office"></div>
    <p class="spec-intro"><b>OUR SPECIALISMS:</b> Our consultants provide a professional and effective service in the supply of the following speciality nurses:</p>
    <ul class="spec-list">
      <li>Theatre (Scrub, Anaesthetics, Recovery) and ODP's</li>
      <li>A&amp;E Nurses</li>
      <li>ITU / HDU / CCU Nurses</li>
      <li>Paediatric Nurses (General Paeds, PICU &amp; NICU)</li>
      <li>RMN &amp; CPN's</li>
      <li>Oncology Nurses</li>
      <li>Community / District Nurses</li>
      <li>Midwives</li>
    </ul>
  </div>
  <div class="abs about body-text">
    <p>Meridian Nursing was established with a sole focus to provide nationwide recruitment solutions for specialist sector nursing requirements. We have over 30 years industry experience and successfully deliver nursing solutions to client requirements.</p>
    <p>Our philosophy is to be masters in our supply of specialist staff rather than diluting our service by over generalising. This ethos was naturally birthed from supplying to all types of healthcare establishments and identifying a trend whereby agencies could fill easier bookings - still leaving the client with those important and hard to fill requirements and ultimately falling short of providing a full service.</p>
  </div>
  <svg class="abs service-clock" width="30" height="30" viewBox="0 0 30 30" aria-hidden="true"><circle cx="15" cy="15" r="12.5" fill="none" stroke="var(--teal)" stroke-width="3"/><path d="M15 8v7h6" fill="none" stroke="var(--teal)" stroke-width="2.5"/></svg>
  <span class="abs service-tag">24 HOUR SERVICE:</span>
  <p class="abs service-text body-text">Our consultants are available 24hrs round the clock to manage requests: Last minute adhoc, long/short term bookings, block bookings and pre-approved rotas.</p>
  <div class="foot-rule"></div>
</section>

<section class="page page--back">
  <div class="abs head-band"><h2>WHY MERIDIAN CARE STAFFING?</h2><h3>Selective Recruitment Drives</h3></div>
  <p class="abs lead body-text"><span class="kick">We recruit</span> for a smaller skill-set than most agencies. This allows serious focus to ensure the best quality nurses are selected to represent our values and provide care for your patients.</p>
  <p class="abs para2 body-text">We have heavily invested in tailoring Meridian Nursing to the important requirements that remain unfilled nationwide. This strategy works hand in hand to alleviate the pressure from staff banks and procurement teams who struggle with supply of a specific speciality requirement to befilled. Meridian Nursing should be the name that is instantly thought of for provision of speciality nurses.</p>
  <h4 class="abs drive-head">Our selective recruitment drive<br>means we:</h4>
  <div class="photo drive-photo" role="img" aria-label="Photo of a smiling nurse in scrubs with arms folded, colleagues behind"></div>
  <div class="abs drive-list body-text">
    <p><b>Identify locations</b> where consistent speciality shifts are required.</p>
    <p><b>Learn from patterns</b> i.e. busiest periods, hard to fill shifts, average amount of speciality staff utilised per week - this understanding allows our recruitment drive to be structured around your needs as a client and enables us to match staff more effectively to your requirements.</p>
  </div>
  <div class="abs market body-text">
    <p><b>Understand the Healthcare Market:</b></p>
    <p>Meridian Nursing is proud that our specialist consultants are the most knowledgeable in their fields. This alone sets our high standards because we know what differentiates a nurse from an excellent nurse. Our excellent nurses service our clients and are more often requested to commit to the hospitals for a longer period of time. Our expert consultants can be trusted to obtain training, inoculations and compliance which is relevant to the speciality they supply to e.g. EPP clearance's / IV's, venepuncture etc.</p>
  </div>
  <div class="abs screen-band">Candidate Screening</div>
  <p class="abs screen-note">All candidates are required to provide original identification:</p>
  <div class="abs screen-band-green">
    <svg class="screen-icon" style="left:35px" width="36" height="36" viewBox="0 0 36 36" aria-hidden="true"><circle cx="18" cy="18" r="16" fill="none" stroke="#fff" stroke-width="1.5"/><rect x="9" y="12" width="16" height="11" fill="none" stroke="#fff" stroke-width="1.5"/><path d="M12 16h7M12 19h5" stroke="#fff" stroke-width="1.5"/><circle cx="25" cy="22" r="3" fill="#fff"/></svg>
    <div class="screen-col" style="left:24px;width:96px">passport and driving licence, appropriate working visa, verified qualifications and training certificates, proof of address and relevant inoculations.</div>
    <svg class="screen-icon" style="left:166px" width="36" height="36" viewBox="0 0 36 36" aria-hidden="true"><circle cx="18" cy="18" r="16" fill="none" stroke="#fff" stroke-width="1.5"/><rect x="11" y="9" width="14" height="18" fill="none" stroke="#fff" stroke-width="1.5"/><path d="M18 13v6M15 16h6M14 23h8" stroke="#fff" stroke-width="1.5"/></svg>
    <div class="screen-col" style="left:141px;width:104px">We ensure every candidate has: a completed registration form and full career history, verified references covering a minimum of five years, a DBS and has fulfilled occupational health checks for fitness-to-work.</div>
    <svg class="screen-icon" style="left:280px" width="36" height="36" viewBox="0 0 36 36" aria-hidden="true"><circle cx="18" cy="18" r="16" fill="none" stroke="#fff" stroke-width="1.5"/><circle cx="17" cy="19" r="8" fill="none" stroke="#fff" stroke-width="1.5"/><circle cx="17" cy="19" r="4" fill="none" stroke="#fff" stroke-width="1.5"/><path d="M17 19l8-8" stroke="#fff" stroke-width="1.5"/></svg>
    <div class="screen-col" style="left:264px;width:96px">Our aim is to be recognised as the industry's benchmark for excellence in nursing personnel supply to public health trusts, private hospitals, nursing homes and residential care.</div>
    <svg class="screen-icon" style="left:393px;top:8px" width="36" height="36" viewBox="0 0 36 36" aria-hidden="true"><circle cx="18" cy="18" r="16" fill="none" stroke="#fff" stroke-width="1.5"/><circle cx="15" cy="21" r="5" fill="none" stroke="#fff" stroke-width="3" stroke-dasharray="2 1.5"/><circle cx="23" cy="13" r="3.5" fill="none" stroke="#fff" stroke-width="2.5" stroke-dasharray="1.5 1.2"/></svg>
    <div class="screen-col" style="left:372px;width:98px;top:50px">Our tailor-made programmes and services are designed around our clients' needs to guarantee they will be delighted with the quality of our service.</div>
  </div>
  <div class="foot-rule"></div>
</section>

</body>
</html>
```